Evergold Fernbark Inc

Industry/Entity Type

Forestry

Contact Information for Business Card

Company name: Evergold Fernbark INC, Contact Info: Rovelio Marquin, Phone # 740 555 0187, Addres: 284 Willowbend Creek Rd, Marrowfield KR 01234, Email: evergoldfernbark@mailbrook.net

```html
<!DOCTYPE html>
<html lang="en">
<head>
<meta charset="utf-8">
<title>Evergold Fernbark Inc – Business Card</title>
<link rel="stylesheet" href="https://fonts.googleapis.com/css2?family=Philosopher:wght@400&display=swap">
<style>
  :root {
    --backdrop: #4f4f51;
    --card: #ffffff;
    --ink: #55555b;
    --rule: #55555b;
  }
  html, body {
    margin: 0;
    padding: 0;
    width: 1200px;
    height: 960px;
    overflow: hidden;
    background: var(--backdrop);
  }
  .business-card {
    position: absolute;
    left: 180px;
    top: 240px;
    width: 840px;
    height: 480px;
    background: var(--card);
    color: var(--ink);
    font-family: "Philosopher", sans-serif;
    text-align: center;
  }
  .business-card p { margin: 0; position: absolute; left: 0; right: 0; line-height: 1; white-space: nowrap; }
  .company-name {
    top: 74px;
    font-size: 64px;
    letter-spacing: 3px;
  }
  .company-suffix {
    top: 144px;
    font-size: 30px;
  }
  .contact-name {
    top: 246px;
    font-size: 38px;
  }
  .contact-phone {
    top: 320px;
    font-size: 28px;
  }
  .contact-email {
    top: 360px;
    font-size: 21px;
  }
  .card-divider {
    position: absolute;
    left: 0;
    right: 0;
    top: 395px;
    height: 4px;
    background: var(--rule);
  }
  .contact-address {
    top: 416px;
    font-size: 22px;
  }
</style>
</head>
<body>
  <section class="business-card">
    <p class="company-name">EVERGOLD FERNBARK</p>
    <p class="company-suffix">INC</p>
    <p class="contact-name">Rovelio Marquin</p>
    <p class="contact-phone">Phone # 740 555 0187</p>
    <p class="contact-email">Email: evergoldfernbark@mailbrook.net</p>
    <div class="card-divider"></div>
    <p class="contact-address">284 Willowbend Creek Rd, Marrowfield KR 01234</p>
  </section>
</body>
</html>
```